Web Design Project

need a website, logo and a matching business Card for design studio. i have a company that works with many companies and i want to offer design services that will be outsourced to craftflock.

this website is totally for the design services. i need it to be simple but very catcgy and trendy, yet MUST BE ELEGENT.

you being a designer will know best what do i require in this website and how it should look and feel..

i dont need many pages, most of the selling work to clients will be face to face, this is just for them to view the sample works.

the company is called "Corvelin, Vividra Studio", so pages i need are: 1- the Studio 2- Folios 3- Contact us( will include company informaiton, and online contact form that should have a drop-down list of all types of designs.

main focus is the folios pages, it needs to have samples of works, the classification of works should be on two basis, by type of design and by designer. client should be able to select a certain designer and send an inquiry. if the customer does that, then i should get all client details and the designer should get a notification that he has been requested though no contact details of client should be given to designer as i want to make sure that those jobs are given to designer through craft flock and this is an invitation for any designer who care to put his works on the website. next to that, if the customer requires a job online then we need to get information on how design should feel and look.

please quote your price to include the website and business card design, A3 head letter and envelope.

Please provide a mock up of your design or a briefing an initial design before asking to be announced as the winner.

my customers are general managers and decision makers.

Business

• ability to filiter works based on type or designer. and website must offer all types of designs included here

```html
<!DOCTYPE html>
<html lang="en">
<head>
<meta charset="utf-8">
<title>Corvelin, Vividra Studio — Folios</title>
<link href="https://fonts.googleapis.com/css2?family=PT+Sans+Narrow:wght@400;700&family=Arimo:wght@400;700&family=Open+Sans:wght@600&display=swap" rel="stylesheet">
<style>
  :root {
    --bar: #222222;
    --brand-red: #b3302f;
    --brand-red-dark: #8f2322;
    --hire-green: #3fa50e;
    --quality-red: #a82a2a;
    --ink: #111111;
    --step-grey: #8a8a8a;
    --blue: #1590cf;
    --blue-dark: #0b6fa8;
    --navy: #1f3f63;
    --heading-grey: #444444;
    --link-red: #d06060;
    --link-blue: #1b6fae;
    --earn-red: #e06552;
    --row-a: #ebebeb;
    --row-b: #f4f4f4;
    --btn-green: #45a811;
    --btn-green-dark: #35880b;
    --footer: #393939;
    --footer-line: #4d4d4d;
    --help-blue: #2db0f0;
    --white: #ffffff;
  }
  * { box-sizing: border-box; margin: 0; padding: 0; }
  html, body { width: 1200px; height: 1079px; overflow: hidden; }
  body { position: relative; background: var(--white); font-family: "Arimo", Arial, sans-serif; color: var(--ink); }

  .top-bar { position: absolute; left: 0; top: 0; width: 1200px; height: 42px; background: var(--bar); }
  .brand-badge {
    position: absolute; left: 67px; top: 0; width: 258px; height: 94px;
    background: var(--brand-red); border-radius: 0 0 4px 4px;
    box-shadow: 2px 4px 6px rgba(0,0,0,.35);
    display: flex; align-items: center; justify-content: center; text-align: center;
    font-family: "PT Sans Narrow", sans-serif; font-weight: 700; font-size: 25px; line-height: 28px; color: var(--white);
    z-index: 2;
  }
  .main-nav { position: absolute; top: 0; left: 0; height: 42px; }
  .main-nav a {
    position: absolute; top: 13px; white-space: nowrap; text-decoration: none;
    font-family: "Open Sans", sans-serif; font-weight: 600; font-size: 13px; color: var(--white);
  }
  .help-link { position: absolute; left: 1024px; top: 11px; display: flex; align-items: center; gap: 8px; font-size: 11px; color: var(--help-blue); text-decoration: none; }
  .help-icon { width: 21px; height: 21px; border-radius: 50%; background: #e8512b; border: 2px solid #f2f2f2; color: var(--white); font-weight: 700; font-size: 12px; display: flex; align-items: center; justify-content: center; }

  .hero-glow { position: absolute; left: 190px; top: 60px; width: 830px; height: 360px; background: radial-gradient(ellipse at center, #e4e4e4 0%, #f3f3f3 40%, rgba(255,255,255,0) 70%); }
  .hero-title {
    position: absolute; left: 0; top: 146px; width: 1200px; text-align: center; white-space: nowrap;
    font-family: "PT Sans Narrow", sans-serif; font-weight: 700; letter-spacing: -0.5px;
  }
  .hero-title .big { font-size: 54px; }
  .hero-title .small { font-size: 30px; }
  .hero-title .green { color: var(--hire-green); }
  .hero-title .red { color: var(--quality-red); }
  .steps { position: absolute; top: 224px; left: 0; }
  .step { position: absolute; white-space: nowrap; display: flex; align-items: center; gap: 7px; font-size: 15px; color: var(--step-grey); }
  .step-num { width: 18px; height: 18px; border-radius: 50%; background: #2a2a2a; color: var(--white); font-size: 11px; font-weight: 700; display: flex; align-items: center; justify-content: center; }

  .cta { position: absolute; top: 290px; height: 66px; border-radius: 3px; display: flex; align-items: center; justify-content: center;
    font-family: "PT Sans Narrow", sans-serif; font-weight: 700; font-size: 29px; color: var(--white); text-decoration: none;
    box-shadow: 0 12px 10px -8px rgba(0,0,0,.25); }
  .cta-designs { left: 322px; width: 267px; background: linear-gradient(#c4393a, var(--brand-red-dark)); border: 2px solid #fff; }
  .cta-designers { left: 622px; width: 277px; background: linear-gradient(#1c9ad8, var(--blue-dark)); }

  .divider { position: absolute; left: 86px; top: 429px; width: 1041px; height: 1px; background: linear-gradient(90deg, rgba(200,200,200,0), #cfcfcf 20%, #cfcfcf 80%, rgba(200,200,200,0)); }

  .section-title { position: absolute; top: 490px; font-family: "PT Sans Narrow", sans-serif; font-weight: 700; font-size: 32px; }
  .designs-title { left: 96px; color: var(--navy); }
  .designer-title { left: 612px; color: var(--heading-grey); }
  .browse-all { position: absolute; top: 503px; font-size: 14px; color: var(--link-red); text-decoration: none; letter-spacing: .5px; }

  .thumb { position: absolute; width: 135px; height: 78px; border: 5px solid var(--white); box-shadow: 0 1px 5px rgba(0,0,0,.4); }

  .designer-table { position: absolute; left: 608px; top: 543px; width: 532px; border-collapse: collapse; font-size: 13px; }
  .designer-table th { height: 29px; text-align: left; font-weight: 700; font-size: 13px; color: var(--ink); }
  .designer-table td { height: 56px; }
  .designer-table tbody tr:nth-child(odd) { background: var(--row-a); }
  .designer-table tbody tr:nth-child(even) { background: var(--row-b); }
  .designer-table .name { padding-left: 13px; width: 135px; }
  .designer-table .name a { color: var(--link-blue); font-weight: 700; font-size: 14px; }
  .designer-table .hired { width: 140px; padding-left: 10px; }
  .designer-table .earn { color: var(--earn-red); font-weight: 700; width: 128px; }
  .send-btn { display: inline-block; width: 124px; height: 30px; line-height: 30px; text-align: center; border-radius: 3px;
    background: linear-gradient(var(--btn-green), var(--btn-green-dark)); color: var(--white); font-weight: 700; font-size: 14px; letter-spacing: .3px; }

  .site-footer { position: absolute; left: 0; top: 949px; width: 1200px; height: 130px; background: var(--footer); }
  .footer-links { position: absolute; left: 82px; top: 42px; font-size: 10px; letter-spacing: 1px; color: var(--white); white-space: nowrap; }
  .footer-links a { color: var(--white); text-decoration: none; }
  .follow { position: absolute; left: 376px; top: 38px; display: flex; align-items: center; gap: 5px; font-size: 10px; font-weight: 700; color: var(--white); }
  .follow .social { width: 16px; height: 16px; border-radius: 2px; }
  .footer-brand { position: absolute; left: 683px; top: 28px; font-family: "PT Sans Narrow", sans-serif; font-weight: 700; font-size: 22px; line-height: 24px; color: #6a6a6a; }
  .footer-line { position: absolute; left: 67px; top: 91px; width: 1074px; height: 1px; background: var(--footer-line); }
  .copyright { position: absolute; left: 79px; top: 100px; font-size: 10px; letter-spacing: .8px; color: #bdbdbd; }
</style>
</head>
<body>
  <header class="top-bar">
    <nav class="main-nav">
      <a href="#" style="left:422px">THE STUDIO</a>
      <a href="#" style="left:563px">FOLIOS</a>
      <a href="#" style="left:675px">CONTACT US</a>
    </nav>
    <a class="help-link" href="#"><span class="help-icon">?</span>Corvelin Help</a>
  </header>
  <div class="brand-badge">Corvelin,<br>Vividra Studio</div>

  <section class="hero">
    <div class="hero-glow"></div>
    <h1 class="hero-title"><span class="big">Looking</span> <span class="small">to</span> <span class="big green">Hire Designers</span> <span class="small">based on their</span> <span class="big red">Quality?</span></h1>
    <div class="steps">
      <div class="step" style="left:225px"><span class="step-num">1</span>Browse Designs/Designer</div>
      <div class="step" style="left:475px"><span class="step-num">2</span>View Design &amp; Profile</div>
      <div class="step" style="left:716px"><span class="step-num">3</span>Hire Designers through Craft Flock</div>
    </div>
    <a class="cta cta-designs" href="#">Browse by Designs</a>
    <a class="cta cta-designers" href="#">Browse by Designers</a>
  </section>

  <div class="divider"></div>

  <section class="by-designs">
    <h2 class="section-title designs-title">View By Designs:</h2>
    <a class="browse-all" href="#" style="left:469px">[ Browse All ]</a>
    <div class="thumb" style="left:88px;top:567px;background:linear-gradient(#5a4f48 0 18%,#e9e4dc 18%,#d9d2c6)" role="img" aria-label="Website design sample in warm beige tones"></div>
    <div class="thumb" style="left:255px;top:567px;background:linear-gradient(#bfe6f3,#e6f6fb 60%,#f2f2f2)" role="img" aria-label="Cartoon website design sample in light blue"></div>
    <div class="thumb" style="left:424px;top:567px;background:linear-gradient(#1c1c1c,#3a3a3a 60%,#7a7068)" role="img" aria-label="Dark furniture showroom website sample"></div>
    <div class="thumb" style="left:88px;top:678px;background:linear-gradient(120deg,#f3ecd6,#e7c98a 50%,#eee)" role="img" aria-label="Illustrated character artwork sample"></div>
    <div class="thumb" style="left:255px;top:678px;background:#12395f" role="img" aria-label="Studio logo design sample on navy"></div>
    <div class="thumb" style="left:424px;top:678px;background:linear-gradient(#c2361c,#8e1f10 55%,#efefef 55%)" role="img" aria-label="Red and black product website sample"></div>
  </section>

  <section class="by-designer">
    <h2 class="section-title designer-title">View By Designer:</h2>
    <a class="browse-all" href="#" style="left:1038px">[ Browse All ]</a>
    <table class="designer-table">
      <thead><tr><th style="padding-left:8px">User Name</th><th># Time Hired</th><th>Earnings</th><th></th></tr></thead>
      <tbody>
        <tr><td class="name"><a href="#">Pixelwright</a></td><td class="hired">103</td><td class="earn">USD 70253</td><td><span class="send-btn">Send Enquery</span></td></tr>
        <tr><td class="name"><a href="#">marcello</a></td><td class="hired">98</td><td class="earn">USD 65832</td><td><span class="send-btn">Send Enquery</span></td></tr>
        <tr><td class="name"><a href="#">qrv20917</a></td><td class="hired">93</td><td class="earn">USD 62267</td><td><span class="send-btn">Send Enquery</span></td></tr>
        <tr><td class="name"><a href="#">tovan07</a></td><td class="hired">85</td><td class="earn">USD 68451</td><td><span class="send-btn">Send Enquery</span></td></tr>
        <tr><td class="name"><a href="#">lumeniK</a></td><td class="hired">72</td><td class="earn">USD 55369</td><td><span class="send-btn">Send Enquery</span></td></tr>
        <tr><td class="name"><a href="#">devarshK</a></td><td class="hired">70</td><td class="earn">USD 51282</td><td><span class="send-btn">Send Enquery</span></td></tr>
      </tbody>
    </table>
  </section>

  <footer class="site-footer">
    <div class="footer-links"><a href="#">THE SUDIO</a> &nbsp;|&nbsp; <a href="#">FOLIOS</a> &nbsp;|&nbsp; <a href="#">CONTACT US</a></div>
    <div class="follow">FOLOW US ON:&nbsp;
      <span class="social" style="background:#3b5b9a"></span>
      <span class="social" style="background:#3fa9dc"></span>
      <span class="social" style="background:#ef7a1a"></span>
    </div>
    <div class="footer-brand">Corvelin,<br>Vividra Studio</div>
    <div class="footer-line"></div>
    <div class="copyright">Copyright 2012. All Rights Reserved.</div>
  </footer>
</body>
</html>
```